Business Card Design Project - The Bridgeway Partners

Company Name - The Bridgeway Partners

We need a unique logo and business cards

We are a team of experienced IT professionals who specialize in providing business value to organizations via the analysis and understanding the challenges of your particular organization. We focus on understanding the challenges first, and execute against your priorities partnering with your highly valued key resources.

Our extensive experience and focus on Agile delivery methodologies help our clients continuously improve and deliver quality solutions. Using this approach we will always deliver the greatest return on your investments.

Target Market(s)

Large organizations IT departments

Industry/Entity Type

Business

Font styles to use
Serif
Sans Serif

Requirements
Should not have
• no pictures

```html
<!DOCTYPE html>
<html lang="en">
<head>
<meta charset="utf-8">
<title>The Bridgeway Partners – Business Card</title>
<link href="https://fonts.googleapis.com/css2?family=Open+Sans:wght@400;600&display=swap" rel="stylesheet">
<style>
  :root {
    --backdrop: #1b1b1d;
    --card: #4b4b4c;
    --stripe: #f2f2f2;
    --accent: #f0901e;
    --text-light: #e6e6e6;
  }
  html, body {
    margin: 0;
    padding: 0;
    width: 1200px;
    height: 757px;
    overflow: hidden;
    background: var(--backdrop);
    font-family: "Open Sans", sans-serif;
  }
  .card {
    position: absolute;
    left: 180px;
    top: 138px;
    width: 840px;
    height: 480px;
    background: var(--card);
    overflow: hidden;
  }
  .card__chevrons {
    position: absolute;
    inset: 0;
  }
  .holder {
    position: absolute;
    left: 252px;
    top: 92px;
  }
  .holder__name {
    margin: 0;
    font-size: 22px;
    font-weight: 600;
    color: var(--accent);
    line-height: 1.1;
  }
  .holder__role {
    margin: 2px 0 0 10px;
    font-size: 15px;
    font-weight: 400;
    color: var(--text-light);
  }
  .brand {
    position: absolute;
    left: 256px;
    top: 172px;
    display: flex;
    align-items: center;
    gap: 10px;
  }
  .brand__mark {
    width: 12px;
    height: 12px;
    background: var(--accent);
    flex: none;
  }
  .brand__name {
    font-size: 22px;
    font-weight: 600;
    color: var(--accent);
    letter-spacing: 1px;
    text-transform: uppercase;
    white-space: nowrap;
  }
  .contacts {
    position: absolute;
    left: 282px;
    top: 246px;
    margin: 0;
    padding: 0;
    list-style: none;
  }
  .contacts__item {
    display: flex;
    align-items: center;
    gap: 16px;
    height: 34px;
    font-size: 15px;
    color: var(--text-light);
  }
  .contacts__icon {
    width: 14px;
    height: 14px;
    fill: var(--accent);
    flex: none;
  }
</style>
</head>
<body>
  <div class="card">
    <svg class="card__chevrons" width="840" height="480" viewBox="0 0 840 480" aria-hidden="true">
      <polyline points="-20,-20 215,240 -20,500" fill="none" stroke="var(--stripe)" stroke-width="42"/>
      <polyline points="860,-20 665,240 860,500" fill="none" stroke="var(--stripe)" stroke-width="42"/>
    </svg>

    <div class="holder">
      <p class="holder__name">Dara Whitlow</p>
      <p class="holder__role">Manager</p>
    </div>

    <div class="brand">
      <span class="brand__mark"></span>
      <span class="brand__name">The Bridgeway Partners</span>
    </div>

    <ul class="contacts">
      <li class="contacts__item">
        <svg class="contacts__icon" viewBox="0 0 24 24" aria-hidden="true"><path d="M6.6 10.8a15.1 15.1 0 0 0 6.6 6.6l2.2-2.2a1 1 0 0 1 1-.25 11.4 11.4 0 0 0 3.6.57 1 1 0 0 1 1 1V20a1 1 0 0 1-1 1A17 17 0 0 1 3 4a1 1 0 0 1 1-1h3.5a1 1 0 0 1 1 1c0 1.25.2 2.45.57 3.570a1 1 0 0 1-.25 1z"/></svg>
        <span>00 987 654 321 00</span>
      </li>
      <li class="contacts__item">
        <svg class="contacts__icon" viewBox="0 0 24 24" aria-hidden="true"><path d="M12 2a10 10 0 1 0 0 20 10 10 0 0 0 0-20zm0 3.5a6.5 6.5 0 1 1 0 13 6.5 6.5 0 0 1 0-13z"/><circle cx="12" cy="12" r="3"/></svg>
        <span>www.bridgewaypartners.com</span>
      </li>
      <li class="contacts__item">
        <svg class="contacts__icon" viewBox="0 0 24 24" aria-hidden="true"><path d="M2 5h20v14H2z M4 7v1l8 5 8-5V7l-8 5z" fill-rule="evenodd"/></svg>
        <span>email:hello@bridgewaypartners.com</span>
      </li>
    </ul>
  </div>
</body>
</html>
```